Business Card/ Email Signature Design Project

I am an Interior Designer. I need a business card that looks sophisticated stylish but simple in design. My work covers space design/ interior architecture/ furniture design/ product development & styling.

I have a very specific brief and know mostly what I want. I'm hoping to work with someone who can translate my ideas.

My branding should have a strong focus on my name, the majority of my work is referral based.
I'm keen to keep a monochromatic colour scheme: dark charcoal/ black/ white/ embossing/ silver. I'm not suggesting we use all that I've listed, they are possible ideas at this stage. I will need to be mindful of printing costs an also how I make the design work across, cards, letter heads, email logo and web design.

Theory behind images sent below;
1-Rug Image_(minus boarder) I was thinking this image could be used on the back of the card with my contact details over. I like that the lines are almost hand drawn and start to look free form. It's a subtle contrast to a more formal front of the card with my name.
2_Owen Ratley_I really like the orientation, the proportion of font on the card, the colour and the font. I like the lower case for my name and the upper case for 'Interior Design'. Not sure if it should be 'Interior Designer or Interior Design' at this stage, was leaning towards 'Interior Design'. Was thinking the 'i' and 'd' in my surname could be the colour eg 'silver'?? We can decide on this once we see it.

Look forward to hearing from you.
Cheers,
Noreen Bastoli

Industry/Entity Type

Printing

Logo Text

Noreen Bastoli Interior Design

```html
<!DOCTYPE html>
<html lang="en">
<head>
<meta charset="utf-8">
<title>Owen Ratley – Business Card</title>
<link rel="stylesheet" href="https://fonts.googleapis.com/css2?family=Federant&family=PT+Sans+Narrow:wght@700&display=swap">
<style>
  :root {
    --canvas-bg: #ececec;
    --ink: #111111;
    --paper: #ffffff;
    --card-grey: #a9aaae;
    --rug-light: #c4bfb6;
    --rug-mid: #aea99f;
    --contact-red: #ee3a3f;
    --silver-light: #f4f4f4;
    --silver-dark: #1a1a1a;
  }
  * { box-sizing: border-box; margin: 0; padding: 0; }
  html, body { width: 1200px; height: 1200px; overflow: hidden; }
  body {
    background: var(--canvas-bg);
    position: relative;
  }
  .card {
    position: absolute;
    left: 190px;
    width: 820px;
    height: 480px;
    border: 3px solid var(--ink);
    overflow: hidden;
  }
  .card--back { top: 50px; background: var(--paper); padding: 6px; }
  .card--front {
    top: 660px;
    background: var(--card-grey);
    border: 6px solid;
    border-image: linear-gradient(90deg, var(--silver-dark), var(--silver-light) 55%, var(--silver-dark)) 1;
  }
  .rug-texture {
    position: absolute;
    inset: 6px;
    background: radial-gradient(ellipse at 40% 45%, var(--rug-light), var(--rug-mid));
  }
  .card-name {
    font-family: "Federant", serif;
    color: var(--ink);
    -webkit-text-stroke: 1px var(--paper);
    white-space: nowrap;
    position: absolute;
    width: 100%;
    text-align: center;
  }
  .card--back .card-name { top: 18px; font-size: 108px; left: 0; width: 812px; }
  .card--front .card-name { top: 128px; font-size: 110px; left: 0; }
  .contact-list {
    position: absolute;
    left: 46px;
    top: 200px;
    list-style: none;
    font-family: "PT Sans Narrow", sans-serif;
    font-weight: 700;
    font-size: 46px;
    line-height: 60px;
    letter-spacing: -1px;
    color: var(--contact-red);
    -webkit-text-stroke: 0.6px var(--paper);
  }
  .title-row {
    position: absolute;
    top: 272px;
    left: 0;
    width: 100%;
    display: flex;
    align-items: center;
    justify-content: center;
    gap: 12px;
  }
  .title-rule {
    width: 140px;
    height: 12px;
    background: linear-gradient(90deg, var(--silver-light), var(--silver-dark));
  }
  .title-rule--right { background: linear-gradient(90deg, var(--silver-dark), var(--silver-light)); }
  .card-title {
    font-family: "Federant", serif;
    font-size: 54px;
    color: var(--ink);
    -webkit-text-stroke: 0.8px var(--paper);
    white-space: nowrap;
  }
</style>
</head>
<body>
  <section class="card card--back" aria-label="Card back">
    <div class="rug-texture" role="img" aria-label="Photograph of a grey rug with loose hand-drawn black linework"></div>
    <h2 class="card-name">Owen Ratley</h2>
    <ul class="contact-list">
      <li>Address:P.O Box 412 Elmswood VIC. 3190</li>
      <li>Email:interior@noreenbastoli.com</li>
      <li>Web:www.noreenbastoli.com</li>
      <li>Mobile: 0400 555 219</li>
    </ul>
  </section>

  <section class="card card--front" aria-label="Card front">
    <h1 class="card-name">Owen Ratley</h1>
    <div class="title-row">
      <span class="title-rule"></span>
      <p class="card-title">Interior Designer</p>
      <span class="title-rule title-rule--right"></span>
    </div>
  </section>
</body>
</html>
```